Lomi-Seret - Promote and Support a community

Design a website for Ethiopean Community. the design should be friendly, easy to navigate and maintain the look & feel of the Ethiopian culture. a proposed logo is attached but it can be change according to your recommendations. This is a project we are doing at a discount rate as it supports a weak community.
Please visit their current website http://www.lomi-seret.example.il/index.php?lang=en

Target Market(s)

Community members, potential doners

Industry/Entity Type

community

Number of Pages Required

1 page

Font styles to use
Sans Serif

Requirements
Must have
• easy to navigate friendly interface

```html
<!DOCTYPE html>
<html lang="en">
<head>
<meta charset="utf-8">
<title>Lomi-Seret – Community</title>
<link href="https://fonts.googleapis.com/css2?family=Poppins:wght@400;500;600;700&family=Open+Sans:wght@400;600&display=swap" rel="stylesheet">
<style>
:root{
  --green:#208a5f;
  --green-dark:#17704c;
  --ink:#2b2b2b;
  --muted:#7a7a7a;
  --dark:#1f1f1f;
  --footer:#2c2c2c;
  --light:#f1f1f1;
  --line:#d6d6d6;
}
*{box-sizing:border-box;margin:0;padding:0}
html,body{width:1200px;height:3190px;overflow:hidden}
body{font-family:"Open Sans",sans-serif;color:var(--ink);background:#fff;position:relative}
.section{position:absolute;left:0;width:1200px}
.abs{position:absolute}
.head{font-family:"Poppins",sans-serif}

/* header */
.site-header{top:0;height:106px;background:#fff}
.brand{left:232px;top:38px;display:flex;align-items:center;gap:8px;font-family:"Poppins",sans-serif;font-weight:700;font-size:15px;color:var(--green)}
.brand-dot{width:14px;height:14px;border-radius:50%;background:var(--green)}
.main-nav{left:342px;top:46px;display:flex;gap:19px;font-family:"Poppins",sans-serif;font-weight:600;font-size:9.5px;letter-spacing:.1px}
.lang-btn{left:885px;top:36px;width:81px;height:32px;background:#111;color:#fff;font-family:"Poppins",sans-serif;font-size:10px;font-weight:600;display:flex;align-items:center;justify-content:center;gap:6px}

/* hero */
.hero{top:106px;height:378px;background:linear-gradient(120deg,#8a2a4a,#c4443f 25%,#3f6bb0 50%,#d8a13a 70%,#7a2c5c)}
.hero-shade{inset:0;background:rgba(0,0,0,.25)}
.hero h1{left:0;width:1200px;top:70px;text-align:center;font-family:"Poppins",sans-serif;font-weight:700;font-size:58px;color:#fff;letter-spacing:-1px}
.hero p{left:300px;width:600px;top:140px;text-align:center;color:#fff;font-size:21px;line-height:30px}
.btn{display:flex;align-items:center;justify-content:center;gap:6px;background:var(--green);color:#fff;font-family:"Poppins",sans-serif;font-weight:600;letter-spacing:1.5px}
.hero .btn{top:264px;height:40px;width:137px;font-size:12px}

/* about */
.about{top:484px;height:512px}
.about-photo{left:590px;top:0;width:610px;height:512px;background:linear-gradient(135deg,#3a2e2a,#6d5a4c 45%,#2f4f6a 70%,#3b8a7c)}
.about .eyebrow{left:64px;top:52px;font-family:"Poppins",sans-serif;font-weight:600;font-size:29px;color:var(--green)}
.about h2{left:64px;top:88px;width:500px;font-family:"Poppins",sans-serif;font-weight:600;font-size:22px;line-height:33px}
.about p{left:64px;top:174px;width:490px;font-size:18.5px;line-height:24px;color:var(--muted)}
.about .btn{left:64px;top:409px;width:136px;height:40px;font-size:12px}

/* cards */
.topics{top:996px;height:401px;background:linear-gradient(180deg,#c9c9c9,#e2e2e2 50%,#cfcfcf)}
.topic-card{top:69px;width:174px;height:267px;background:#fff;padding:4px}
.topic-img{height:165px}
.topic-card h3{font-family:"Poppins",sans-serif;font-size:9.5px;font-weight:600;margin:18px 6px 6px}
.topic-card p{font-family:"Poppins",sans-serif;font-size:8px;line-height:14px;margin:0 6px;color:#333}
.topic-card .more{font-family:"Poppins",sans-serif;font-size:8px;font-weight:600;margin:8px 6px}

/* partners */
.partners{top:1397px;height:201px}
.badge{top:48px;width:70px;height:70px;background:#e6ecef;border-radius:6px}

/* testimonials */
.testimonials{top:1598px;height:372px;background:var(--dark);color:#fff;text-align:center}
.testimonials h2{left:0;width:1200px;top:34px;font-family:"Poppins",sans-serif;font-weight:600;font-size:28px}
.rule{left:475px;top:82px;width:250px;height:1px;background:#555}
.rule-bold{left:565px;top:80px;width:70px;height:3px;background:#fff}
.quote-mark{font-family:"Poppins",sans-serif;font-weight:700;font-size:70px;line-height:1;color:#ddd}
.testimonials .lead{left:275px;width:650px;top:110px;font-family:"Poppins",sans-serif;font-weight:600;font-size:14.5px;line-height:18px}
.testimonials .body{left:275px;width:650px;top:162px;font-family:"Poppins",sans-serif;font-weight:500;font-size:9.5px;line-height:17px}
.testimonials .name{left:0;width:1200px;top:265px;font-family:"Poppins",sans-serif;font-size:12px}
.testimonials .role{left:0;width:1200px;top:284px;font-size:8.5px;font-style:italic;color:#ccc}
.dots{left:585px;top:314px;display:flex;gap:4px}
.dots i{width:7px;height:7px;border-radius:50%;border:1px solid #fff}
.dots i.on{background:#fff}

/* news */
.news{top:1970px;height:570px}
.news h2{left:0;width:1200px;top:42px;text-align:center;font-family:"Poppins",sans-serif;font-weight:700;font-size:29px;color:var(--green);letter-spacing:1px}
.news .intro{left:370px;width:460px;top:98px;text-align:center;font-family:"Poppins",sans-serif;font-size:10px;line-height:15px;color:var(--muted)}
.news-card{top:164px;width:232px}
.news-img{height:200px}
.news-card h3{font-family:"Poppins",sans-serif;font-size:12px;font-weight:600;letter-spacing:.6px;margin:16px 1px 12px}
.news-card p{font-family:"Poppins",sans-serif;font-size:9px;line-height:17.5px;color:var(--muted);width:205px;margin-left:1px}
.news-card .btn{width:73px;height:25px;font-size:7px;letter-spacing:.3px;margin-top:14px;margin-left:1px}

/* contact */
.contact{top:2540px;height:346px;background:var(--light)}
.contact h2{left:0;width:1190px;top:34px;text-align:center;font-family:"Poppins",sans-serif;font-weight:600;font-size:25px}
.field{border:1px solid #c8c8c8;background:#f7f7f7;font-family:"Poppins",sans-serif;font-size:8px;color:#999;padding:6px 10px}
.contact .submit{left:549px;top:275px;width:91px;height:25px;font-size:8.5px;letter-spacing:0}

/* footer */
.site-footer{top:2886px;height:249px;background:var(--footer);color:#fff}
.col-title{font-family:"Poppins",sans-serif;font-size:13px}
.col-rule{top:34px;width:160px;height:1px;background:#555}
.col-rule-b{top:33px;width:32px;height:2px;background:#fff}
.foot-text{font-family:"Poppins",sans-serif;font-size:8px;line-height:15px;color:#ddd}
.link-list{list-style:none;font-family:"Poppins",sans-serif;font-size:8px;color:#ddd}
.link-list li{height:21px}
.link-list li::before{content:"›";margin-right:10px}
.info-row{display:flex;gap:16px;height:21px;align-items:flex-start;font-family:"Poppins",sans-serif;font-size:8px;color:#ddd}
.info-row svg{width:9px;height:9px;flex:none}
.socials{display:flex;gap:12px}
.socials i{width:9px;height:9px;border-radius:50%;background:#bbb}
.copyright{top:3135px;height:55px;background:var(--green);color:#fff;font-family:"Poppins",sans-serif;font-size:8.5px;display:flex;align-items:center;justify-content:center}
</style>
</head>
<body>

<header class="section site-header">
  <div class="abs brand"><span class="brand-dot"></span>Lomi-Seret</div>
  <nav class="abs main-nav">
    <span>HOME</span><span>ABOUT</span><span>THE COMMUNITY</span><span>PROGRAMS</span><span>NEWS</span><span>ADVOCACY</span><span>PARTNERS</span><span>SUPPORT US</span>
  </nav>
  <div class="abs lang-btn">English
    <svg width="8" height="8" viewBox="0 0 8 8"><circle cx="4" cy="4" r="4" fill="#fff"/><path d="M3 2l2 2-2 2" stroke="#111" stroke-width="1.2" fill="none"/></svg>
  </div>
</header>

<section class="section hero" role="img" aria-label="Colourful woven Ethiopian baskets">
  <div class="abs hero-shade"></div>
  <h1 class="abs">WELCOME LOMI-SERET</h1>
  <p class="abs">Lorem Ipsum is simply dummy text of the printing and typesetting industry. Lorem Ipsum has been the industry's standard dummy text ever since the</p>
  <div class="abs btn" style="left:438px">READ MORE</div>
  <div class="abs btn" style="left:593px">CONTACT US</div>
</section>

<section class="section about">
  <div class="abs about-photo" role="img" aria-label="Young community members gathered around a table"></div>
  <div class="abs eyebrow">ABOUT US</div>
  <h2 class="abs">LOREM IPSUM IS SIMPLY DUMMY TEXT OF THE PRINTING AND TYPESETTING INDUSTRY.</h2>
  <p class="abs">Lorem Ipsum is simply dummy text of the printing and typesetting industry. Lorem Ipsum has been the industry's standard dummy text ever since the 1500s, when an unknown printer took a galley of type and scrambled it to make a type specimen book. It has survived not only five centuries, but alsothe leap into electronic typesetting, remaining essentially unchanged. It was popularised in the</p>
  <div class="abs btn">READ MORE
    <svg width="10" height="10" viewBox="0 0 10 10"><circle cx="5" cy="5" r="5" fill="#fff"/><path d="M4 3l2 2-2 2" stroke="#208a5f" stroke-width="1.4" fill="none"/></svg>
  </div>
</section>

<section class="section topics" role="img" aria-label="Faded photo of community elders in the background">
  <article class="abs topic-card" style="left:234px">
    <div class="topic-img" role="img" aria-label="Elder in a blue knit hat" style="background:linear-gradient(160deg,#3a4a8a,#8a7a6a 50%,#d9d6cf)"></div>
    <h3>THE COMMUNITY</h3><p>Lorem Ipsum is simply dummy text of the printing and typesetting industry.</p><div class="more">READ MORE</div>
  </article>
  <article class="abs topic-card" style="left:420px">
    <div class="topic-img" role="img" aria-label="Audience wearing white shawls" style="background:linear-gradient(160deg,#5a3a2a,#8a5a3a 45%,#e0d6c6)"></div>
    <h3>PROGRAMS</h3><p>Lorem Ipsum is simply dummy text of the printing and typesetting industry.</p><div class="more">READ MORE</div>
  </article>
  <article class="abs topic-card" style="left:605px">
    <div class="topic-img" role="img" aria-label="Lecture hall with a projected presentation" style="background:linear-gradient(160deg,#e8e8e0,#8a4a3a 45%,#2a2a2a)"></div>
    <h3>ADVOCACY</h3><p>Lorem Ipsum is simply dummy text of the printing and typesetting industry.</p><div class="more">READ MORE</div>
  </article>
  <article class="abs topic-card" style="left:791px">
    <div class="topic-img" role="img" aria-label="Speaker addressing a seated group" style="background:linear-gradient(160deg,#4a5a6a,#b8b8b0 45%,#3a3a3a)"></div>
    <h3>THE COMMUNITY</h3><p>Lorem Ipsum is simply dummy text of the printing and typesetting industry.</p><div class="more">READ MORE</div>
  </article>
</section>

<section class="section partners" aria-label="Partners">
  <div class="abs badge" style="left:251px"></div>
  <div class="abs badge" style="left:414px;height:40px;top:63px;width:80px"></div>
  <div class="abs badge" style="left:580px;width:84px;height:60px;top:53px"></div>
  <div class="abs badge" style="left:735px;width:90px;height:50px;top:58px"></div>
  <div class="abs badge" style="left:905px;width:52px;height:84px;top:42px"></div>
</section>

<section class="section testimonials">
  <h2 class="abs">TESTIMONIALS</h2>
  <div class="abs rule"></div><div class="abs rule-bold"></div>
  <div class="abs quote-mark" style="left:233px;top:106px">“</div>
  <div class="abs quote-mark" style="left:938px;top:218px">”</div>
  <p class="abs lead">Lorem ipsum dolor sit amet, consectetur adipisicing elit, sed do eiusmod tempor incididunt ut labore et dolore magna aliqua. Ut enim ad minim veniam, quis nostrud exercitation</p>
  <p class="abs body">Lorem ipsum dolor sit amet, consectetur adipisicing elit, sed do eiusmod tempor incididunt ut labore et dolore magna aliqua. Ut enim ad minim veniam, quis nostrud exercitation ullamco laboris nisi ut aliquip ex ea commodo consequat. Duis aute irure dolor in reprehenderit in voluptate velit esse cillum dolore eu fugiat nulla pariatur. Excepteur sint occaecat cupidatat non proident, sunt in culpa qui officia deserunt mollit anim id est laborum. Sed ut perspiciatis unde omnis iste natus error sit voluptatem accusantium doloremque laudantium, totam rem aperiam, eaque ipsa quae ab illo inventore veritatis et quasi architecto beatae vitae dicta sunt explicabo. Nemo</p>
  <div class="abs name">DANA MELKAMU</div>
  <div class="abs role">Fouder &amp; CEO Kedem Works Ltd.,</div>
  <div class="abs dots"><i class="on"></i><i></i><i></i></div>
</section>

<section class="section news">
  <h2 class="abs">LATEST NEWS</h2>
  <p class="abs intro">Aenean sollicitudin, lorem quis bibendum auctor, nisi elit consequat ipsum, nec sagittis sem nibh id elit. Duis sed odio sit amet nibh vulputate cursus</p>
  <article class="abs news-card" style="left:234px">
    <div class="news-img" role="img" aria-label="Speaker in white shirt addressing a gathering" style="background:linear-gradient(160deg,#4a5a6a,#c8c4bc 45%,#3a3030)"></div>
    <h3>LOREM IPSUM SIMPLY DUMMY</h3>
    <p>Neque porro quisquam est, qui dolorem ipsum quia dolor sit amet, consectetur, adipisci velit, sed quia non numquam eius modi tempora incidunt ut labore et dolore magnam aliquam quaerat voluptatem.</p>
    <div class="btn">READ MORE</div>
  </article>
  <article class="abs news-card" style="left:484px">
    <div class="news-img" role="img" aria-label="Elder woman in a headscarf and white shawl" style="background:linear-gradient(160deg,#2a2622,#6a4a30 45%,#e8e6e0)"></div>
    <h3>LOREM IPSUM SIMPLY DUMMY</h3>
    <p>zNeque porro quisquam est, qui dolorem ipsum quia dolor sit amet, consectetur, adipisci velit, sed quia non numquam eius modi tempo-ra incidunt ut labore et dolore magnam aliquam quaerat voluptatem.</p>
    <div class="btn">READ MORE</div>
  </article>
  <article class="abs news-card" style="left:734px">
    <div class="news-img" role="img" aria-label="Two elders in white caps" style="background:linear-gradient(160deg,#3a4a30,#b0a898 45%,#e8e8ec)"></div>
    <h3>LOREM IPSUM SIMPLY DUMMY</h3>
    <p>Neque porro quisquam est, qui dolorem ipsum quia dolor sit amet, consectetur, adipisci velit, sed quia non numquam eius modi tempora incidunt ut labore et dolore magnam aliquam quaerat voluptatem.</p>
    <div class="btn">READ MORE</div>
  </article>
</section>

<section class="section contact">
  <h2 class="abs">CONTACT US</h2>
  <div class="abs field" style="left:231px;top:88px;width:225px;height:24px">Name</div>
  <div class="abs field" style="left:480px;top:88px;width:226px;height:24px">Phone</div>
  <div class="abs field" style="left:735px;top:88px;width:225px;height:24px">Email</div>
  <div class="abs field" style="left:231px;top:135px;width:729px;height:118px">Message</div>
  <div class="abs btn submit">SUBMIT</div>
</section>

<footer class="section site-footer">
  <div class="abs col-title" style="left:235px;top:44px">About Us</div>
  <div class="abs col-rule" style="left:235px;top:74px;width:182px"></div><div class="abs col-rule-b" style="left:235px;top:73px"></div>
  <p class="abs foot-text" style="left:235px;top:98px;width:230px">Lorem ipsum dolor sit amet, consectetur adipisicing elit, sed do eiusmod tempor incididunt ut labore et dolore magna aliqua. Ut enim ad minim veniam, quis nostrud exercitation ullamco laboris nisi ut aliquip ex ea commodo consequat. Duis aute irure dolor in reprehenderit in voluptate velit esse cillum dolore eu</p>
  <div class="abs socials" style="left:236px;top:204px"><i></i><i></i><i></i><i></i><i></i><i></i></div>

  <div class="abs col-title" style="left:485px;top:44px">Infomation</div>
  <div class="abs col-rule" style="left:485px;top:74px;width:232px"></div><div class="abs col-rule-b" style="left:485px;top:73px"></div>
  <ul class="abs link-list" style="left:485px;top:100px"><li>Home</li><li>About Us</li><li>The Community</li><li>Programs</li><li>Testimonials</li></ul>
  <ul class="abs link-list" style="left:611px;top:100px"><li>Advocacy</li><li>Partners</li><li>Support Us</li></ul>

  <div class="abs col-title" style="left:735px;top:44px">Field Office</div>
  <div class="abs col-rule" style="left:735px;top:74px;width:230px"></div><div class="abs col-rule-b" style="left:735px;top:73px"></div>
  <div class="abs" style="left:735px;top:99px">
    <div class="info-row"><svg viewBox="0 0 10 10"><path d="M5 0a3.5 3.5 0 0 0-3.5 3.5C1.5 6 5 10 5 10s3.5-4 3.5-6.5A3.5 3.5 0 0 0 5 0z" fill="#fff"/><circle cx="5" cy="3.5" r="1.2" fill="#2c2c2c"/></svg>Tamar 12/4 POB 4410 Galim, 40210</div>
    <div class="info-row"><svg viewBox="0 0 10 10"><path d="M2 0l2 2.5-1.2 1.2a6 6 0 0 0 3.5 3.5L7.5 6 10 8l-1.5 2C4 10 0 6 0 1.5z" fill="#fff"/></svg>04-5550172</div>
    <div class="info-row"><svg viewBox="0 0 10 10"><rect y="1.5" width="10" height="7" fill="#fff"/><path d="M0 1.5l5 4 5-4" stroke="#2c2c2c" fill="none"/></svg>hello@lomi-seret.example.il</div>
    <div class="info-row"><svg viewBox="0 0 10 10"><rect x="0" y="3" width="10" height="6" fill="#fff"/><rect x="2" y="0" width="6" height="3" fill="#fff"/><rect x="2.5" y="5" width="5" height="1" fill="#2c2c2c"/></svg>04-5550172</div>
    <div class="info-row"><svg viewBox="0 0 10 10"><circle cx="5" cy="5" r="4.3" stroke="#fff" stroke-width="1.2" fill="none"/><path d="M5 2.5V5h2" stroke="#fff" fill="none"/></svg>Mon - Sat: 9:00 - 18:00</div>
  </div>
</footer>

<div class="section copyright">© Copyrights 2022 Lomi-Seret. All rights reserved.</div>

</body>
</html>
```